Recruiting ad for Caregivers and Nurses

We need a few amazing, fun, catchy, creative recruiting ads for Caregivers and Nurses to care for homecare patients on the island of Oahu, in Hawaii. We are an in home care company called Brantley Homecare. Our care services are provided 24/7, so we need staff that can work days, nights, weekdays, weekends. We need catchy fun ads to entice caregivers and nurses to call our office to inquire about jobs available. Our patients age range is from babies to seniors. We need caregivers and nurses for basic patient care (bathing, dressing, ambulating, preparing meals, medication reminders, light housekeeping) and complex patients (oxygen, tube feeding, injections, vents, wound care). Here are some bullets to consider including:
*Full-time and Part-time Positions Available (days, nights, weekdays, weekends)
*Sign-On Bonus Programs Offered up to $500
*Refer a Friend Bonus Program
*Holiday Pay
*2 Health Plans to Choose from
*Island-Wide Locations
*All PPE Provided (masks, gloves, etc)
*401K Program
*Tuition Benefits

```html
<!DOCTYPE html>
<html lang="en">
<head>
<meta charset="utf-8">
<title>Brantley Homecare – We Are Hiring</title>
<link rel="stylesheet" href="https://fonts.googleapis.com/css2?family=Lato:wght@400;700;900&family=Montserrat:ital,wght@1,900&family=Oswald:wght@400;500;600;700&display=swap">
<style>
  :root{
    --page:#ffffff;
    --paper:#f4f4f4;
    --ink:#231f20;
    --ink-soft:#2e1d18;
    --teal:#1a96ac;
    --teal-bright:#00b5c9;
    --teal-deep:#119aa9;
    --forest:#0b8a72;
    --lime:#a9c94b;
    --salmon:#f49c82;
    --blush:#f7c4b5;
    --box-line:#6e3a2c;
    --photo-room:#d9b78a;
    --photo-scrubs:#7fcde3;
    --white:#ffffff;
  }
  *{margin:0;padding:0;box-sizing:border-box;}
  html,body{width:990px;height:1200px;overflow:hidden;background:var(--page);}
  .canvas{position:relative;width:990px;height:1200px;background:var(--page);}
  .flyer{position:absolute;left:162px;top:169px;width:665px;height:861px;overflow:hidden;background:var(--paper);font-family:"Lato",sans-serif;}
  .flyer-art{position:absolute;inset:0;width:665px;height:861px;}
  .brand{position:absolute;left:30px;top:53px;width:220px;text-align:center;color:var(--ink);font-family:"Lato",sans-serif;font-weight:900;}
  .brand-mark{display:block;width:57px;height:57px;margin:0 auto 14px;background:var(--ink);border-radius:8px;}
  .brand-name{display:block;font-size:40px;line-height:1;letter-spacing:-0.5px;}
  .brand-sub{display:block;font-size:12px;letter-spacing:8px;margin-top:7px;}
  .offer-box{position:absolute;left:55px;top:486px;width:270px;height:210px;border:1.5px solid var(--box-line);border-radius:6px;text-align:center;color:var(--ink);font-family:"Oswald",sans-serif;box-shadow:0 12px 10px -10px rgba(90,40,30,.45);}
  .offer-hours{margin-top:12px;font-weight:700;font-size:58px;line-height:54px;letter-spacing:0.5px;}
  .offer-tag{display:inline-block;margin-top:6px;width:232px;background:var(--white);font-weight:600;font-size:25px;line-height:36px;}
  .offer-shifts{margin-top:6px;font-weight:400;font-size:17px;letter-spacing:-0.2px;}
  .perks{position:absolute;left:355px;top:487px;width:300px;list-style:none;color:var(--ink-soft);font-size:14.5px;font-weight:700;}
  .perks li{position:relative;padding-left:21px;line-height:17.5px;margin-bottom:6px;}
  .perks li svg{position:absolute;left:0;top:2px;width:13px;height:13px;}
  .contact{position:absolute;left:0;top:760px;width:665px;height:90px;color:var(--white);}
  .contact-address{position:absolute;left:50px;top:0;width:258px;text-align:center;font-size:17px;font-weight:700;line-height:22px;}
  .contact-address .pin-row{display:flex;align-items:center;justify-content:center;gap:14px;height:24px;margin-bottom:6px;}
  .contact-address .rule{width:60px;height:1px;background:var(--white);opacity:.8;}
  .contact-divider{position:absolute;left:317px;top:13px;width:2px;height:60px;background:var(--white);}
  .contact-reach{position:absolute;left:338px;top:12px;font-weight:900;line-height:34px;}
  .contact-phone{font-size:30.5px;}
  .contact-web{font-size:25.5px;font-weight:700;}
</style>
</head>
<body>
<div class="canvas">
  <div class="flyer">
    <svg class="flyer-art" viewBox="0 0 665 861" xmlns="http://www.w3.org/2000/svg">
      <defs>
        <linearGradient id="photoTone" x1="0" y1="0" x2="0" y2="1">
          <stop offset="0" stop-color="var(--photo-room)"/>
          <stop offset="1" stop-color="var(--photo-scrubs)"/>
        </linearGradient>
      </defs>
      <!-- photo frame ring -->
      <circle cx="462" cy="155" r="224" fill="var(--blush)"/>
      <circle cx="462" cy="155" r="206" fill="var(--white)"/>
      <circle cx="462" cy="155" r="198" fill="var(--photo-room)" role="img" aria-label="Photo of a caregiver in blue scrubs chatting with a smiling client on a sofa in a bright living room"/>
      <!-- waves -->
      <path d="M0 322 C60 305 120 318 190 340 C260 360 300 380 360 395 C450 420 560 390 665 320 L665 470 L0 470 Z" fill="var(--forest)"/>
      <path d="M0 410 C100 380 230 390 318 407 C380 420 400 452 460 456 C540 460 610 430 665 405 L665 861 L0 861 Z" fill="var(--salmon)" stroke="var(--white)" stroke-width="3"/>
      <!-- foreground photo area -->
      <path d="M325 452 L360 300 L640 300 L665 330 L665 405 C610 430 540 460 460 458 C400 457 360 456 325 452 Z" fill="url(#photoTone)" role="img" aria-label="Photo of a smiling nurse in light blue scrubs with a stethoscope"/>
      <!-- bottom band -->
      <path d="M0 713 C70 735 140 748 210 746 C300 742 370 712 440 715 C540 718 610 740 665 760 L665 861 L0 861 Z" fill="var(--teal-deep)" stroke="var(--white)" stroke-width="3"/>
      <path d="M0 748 C120 770 240 772 330 752 C430 730 540 745 665 790 L665 861 L0 861 Z" fill="var(--teal-bright)"/>
      <!-- decoration -->
      <circle cx="89" cy="224" r="11" fill="var(--lime)"/>
      <circle cx="133" cy="230" r="3.5" fill="none" stroke="var(--teal)" stroke-width="1.5"/>
      <circle cx="170" cy="222" r="3" fill="var(--lime)"/>
      <circle cx="320" cy="278" r="11" fill="var(--lime)"/>
      <circle cx="60" cy="311" r="6" fill="var(--lime)"/>
      <circle cx="317" cy="390" r="4" fill="none" stroke="var(--teal)" stroke-width="1.5"/>
      <circle cx="323" cy="348" r="2.5" fill="var(--lime)"/>
      <circle cx="78" cy="442" r="2.5" fill="var(--lime)"/>
      <path d="M211 220 h8 M215 216 v8 M46 348 h8 M50 344 v8 M280 427 h8 M284 423 v8" stroke="var(--teal)" stroke-width="1.3"/>
      <path d="M246 215 q4 -5 8 0 t8 0 t8 0 t8 0 t8 0" fill="none" stroke="var(--teal)" stroke-width="1.8"/>
      <path d="M78 462 q4 -5 8 0 t8 0 t8 0 t8 0 t8 0" fill="none" stroke="var(--teal)" stroke-width="1.8"/>
      <!-- hiring banner -->
      <path d="M62 248 L306 221 L296 290 L75 297 Z" fill="none" stroke="var(--teal)" stroke-width="1.2"/>
      <path d="M71 254 L306 223 L292 287 L82 293 Z" fill="var(--teal)"/>
      <text x="104" y="283" font-family="Montserrat,sans-serif" font-style="italic" font-weight="900" font-size="43" fill="var(--white)" textLength="172" lengthAdjust="spacingAndGlyphs" transform="rotate(-4 190 265)">WE ARE</text>
      <path d="M84 299 L294 290 L312 312 L102 318 Z" fill="var(--lime)"/>
      <path d="M56 317 L316 299 L302 398 L52 430" fill="none" stroke="var(--teal)" stroke-width="1.2"/>
      <path d="M78 320 L312 302 L300 395 L57 432 Z" fill="var(--teal)"/>
      <text x="126" y="404" font-family="Oswald,sans-serif" font-weight="700" font-size="92" fill="var(--white)" textLength="206" lengthAdjust="spacingAndGlyphs" transform="rotate(-5 190 370) skewX(-6)">HIRING</text>
      <path d="M111 417 L269 399 L269 421 L102 442 Z" fill="var(--lime)"/>
      <text x="118" y="436" font-family="Montserrat,sans-serif" font-style="italic" font-weight="900" font-size="15" fill="var(--white)" textLength="134" transform="rotate(-6 190 428)">JOIN OUR TEAM</text>
    </svg>

    <div class="brand">
      <span class="brand-mark"></span>
      <span class="brand-name">Brantley</span>
      <span class="brand-sub">HOMECARE</span>
    </div>

    <div class="offer-box">
      <div class="offer-hours">FULL-TIME<br>PART-TIME</div>
      <div class="offer-tag">POSITIONS AVAILABLE</div>
      <div class="offer-shifts">(DAYS, NIGHTS, WEEKDAYS, WEEKENDS)</div>
    </div>

    <ul class="perks">
      <li><svg viewBox="0 0 14 14"><circle cx="7" cy="7" r="6" fill="none" stroke="var(--ink-soft)" stroke-width="1"/><path d="M4.2 7.2 L6.2 9 L9.8 5" fill="none" stroke="var(--ink-soft)" stroke-width="1.1"/></svg>Sign-On Bonus Programs Offered<br>up to $500</li>
      <li><svg viewBox="0 0 14 14"><circle cx="7" cy="7" r="6" fill="none" stroke="var(--ink-soft)" stroke-width="1"/><path d="M4.2 7.2 L6.2 9 L9.8 5" fill="none" stroke="var(--ink-soft)" stroke-width="1.1"/></svg>Refer a Friend Bonus Program</li>
      <li><svg viewBox="0 0 14 14"><circle cx="7" cy="7" r="6" fill="none" stroke="var(--ink-soft)" stroke-width="1"/><path d="M4.2 7.2 L6.2 9 L9.8 5" fill="none" stroke="var(--ink-soft)" stroke-width="1.1"/></svg>Holiday Pay</li>
      <li><svg viewBox="0 0 14 14"><circle cx="7" cy="7" r="6" fill="none" stroke="var(--ink-soft)" stroke-width="1"/><path d="M4.2 7.2 L6.2 9 L9.8 5" fill="none" stroke="var(--ink-soft)" stroke-width="1.1"/></svg>2 Health Plans to Choose from</li>
      <li><svg viewBox="0 0 14 14"><circle cx="7" cy="7" r="6" fill="none" stroke="var(--ink-soft)" stroke-width="1"/><path d="M4.2 7.2 L6.2 9 L9.8 5" fill="none" stroke="var(--ink-soft)" stroke-width="1.1"/></svg>Island-Wide Locations</li>
      <li><svg viewBox="0 0 14 14"><circle cx="7" cy="7" r="6" fill="none" stroke="var(--ink-soft)" stroke-width="1"/><path d="M4.2 7.2 L6.2 9 L9.8 5" fill="none" stroke="var(--ink-soft)" stroke-width="1.1"/></svg>All PPE Provided (masks, gloves, etc)</li>
      <li><svg viewBox="0 0 14 14"><circle cx="7" cy="7" r="6" fill="none" stroke="var(--ink-soft)" stroke-width="1"/><path d="M4.2 7.2 L6.2 9 L9.8 5" fill="none" stroke="var(--ink-soft)" stroke-width="1.1"/></svg>401K Program</li>
      <li><svg viewBox="0 0 14 14"><circle cx="7" cy="7" r="6" fill="none" stroke="var(--ink-soft)" stroke-width="1"/><path d="M4.2 7.2 L6.2 9 L9.8 5" fill="none" stroke="var(--ink-soft)" stroke-width="1.1"/></svg>Tuition Benefits</li>
    </ul>

    <div class="contact">
      <div class="contact-address">
        <div class="pin-row">
          <span class="rule"></span>
          <svg width="13" height="20" viewBox="0 0 13 20"><path d="M6.5 1 C3.5 1 1.5 3.2 1.5 6 C1.5 9.5 6.5 14 6.5 14 C6.5 14 11.5 9.5 11.5 6 C11.5 3.2 9.5 1 6.5 1 Z" fill="none" stroke="var(--white)" stroke-width="1.4"/><circle cx="6.5" cy="6" r="1.8" fill="var(--white)"/><path d="M2 18 H11" stroke="var(--white)" stroke-width="1.4"/></svg>
          <span class="rule"></span>
        </div>
        4870 Kalani Way,<br>Suite 210 Honolulu HI, 96801
      </div>
      <div class="contact-divider"></div>
      <div class="contact-reach">
        <div class="contact-phone">Call: 808-555-0142</div>
        <div class="contact-web">www.BrantleyCare.com</div>
      </div>
    </div>
  </div>
</div>
</body>
</html>
```